Marketing firm Studio 847
Business card and stationery
Project: Marketing firm Studio 847
Marketing firm Studio 847  -
Creative Brief
Professional
Martin Kovalenko
Marketer, Business Strategist
Derveni, 14, 2385, Strovolia Nicosia Cyprus
Martin@studio-847.com
Www.studio-847.com
I need the logo and the dog on both, business cards and stationery. I need embossed logo or dog but I am also open to other designs.
He logo and the dog but I am also open to new design

```html
<!DOCTYPE html>
<html lang="en">
<head>
<meta charset="utf-8">
<title>Studio 847 — Business Card</title>
<link rel="stylesheet" href="https://fonts.googleapis.com/css2?family=Arimo:ital,wght@0,400;0,700;1,700&family=Tinos:wght@400&display=swap">
<style>
  :root {
    --backdrop: #3a3a3a;
    --card: #ffffff;
    --ink: #1a1a1a;
    --muted: #4a4a4a;
    --purple: #8e4f9e;
    --purple-light: #b98bc6;
    --purple-dark: #6e3a80;
    --band: #111111;
    --rule: #9a9a9a;
  }
  html, body {
    margin: 0;
    padding: 0;
    width: 1200px;
    height: 780px;
    overflow: hidden;
    background: var(--backdrop);
  }
  .canvas {
    position: relative;
    width: 1200px;
    height: 780px;
  }
  .card {
    position: absolute;
    left: 40px;
    top: 50px;
    width: 1120px;
    height: 680px;
    background: var(--card);
    border-radius: 40px;
    overflow: hidden;
  }
  .card__waves {
    position: absolute;
    inset: 0;
  }
  .brand {
    position: absolute;
    left: 260px;
    top: 90px;
    display: flex;
    align-items: center;
    gap: 22px;
  }
  .brand__dot {
    width: 34px;
    height: 34px;
    border-radius: 50%;
    background: var(--purple);
  }
  .brand__name {
    font-family: "Arimo", Arial, sans-serif;
    font-weight: 700;
    font-size: 118px;
    letter-spacing: 2px;
    color: var(--ink);
    line-height: 1;
  }
  .person {
    position: absolute;
    right: 610px;
    top: 350px;
    text-align: right;
  }
  .person__name {
    font-family: "Arimo", Arial, sans-serif;
    font-weight: 700;
    font-size: 34px;
    color: var(--purple);
    margin: 0 0 6px;
  }
  .person__role {
    font-family: "Arimo", Arial, sans-serif;
    font-weight: 700;
    font-style: italic;
    font-size: 24px;
    color: var(--ink);
    margin: 0 0 12px;
  }
  .person__address {
    font-family: "Tinos", "Times New Roman", serif;
    font-size: 24px;
    line-height: 1.3;
    color: var(--muted);
    margin: 0;
    font-style: normal;
  }
  .divider {
    position: absolute;
    left: 540px;
    top: 345px;
    width: 2px;
    height: 160px;
    background: var(--rule);
  }
  .contact {
    position: absolute;
    left: 568px;
    top: 348px;
    margin: 0;
    padding: 0;
    list-style: none;
    font-family: "Tinos", "Times New Roman", serif;
    font-size: 25px;
    color: var(--ink);
  }
  .contact__item {
    display: flex;
    align-items: center;
    gap: 14px;
    height: 44px;
  }
  .contact__icon {
    width: 22px;
    height: 22px;
    flex: none;
    fill: var(--purple);
  }
  .contact__at {
    width: 22px;
    font-family: "Arimo", Arial, sans-serif;
    font-weight: 700;
    font-size: 22px;
    color: var(--purple);
    text-align: center;
  }
  .website {
    position: absolute;
    left: 430px;
    top: 612px;
    font-family: "Tinos", "Times New Roman", serif;
    font-size: 28px;
    color: #ffffff;
  }
</style>
</head>
<body>
<div class="canvas">
  <section class="card">
    <svg class="card__waves" viewBox="0 0 1120 680" aria-hidden="true">
      <defs>
        <linearGradient id="waveTone" x1="0" y1="0" x2="1" y2="0">
          <stop offset="0" stop-color="var(--purple-light)"/>
          <stop offset="0.6" stop-color="var(--purple)"/>
          <stop offset="1" stop-color="var(--purple-dark)"/>
        </linearGradient>
      </defs>
      <path d="M0,575 C300,600 720,540 1120,380 L1120,680 L0,680 Z" fill="url(#waveTone)"/>
      <path d="M0,612 C360,640 760,575 1120,440 L1120,680 L0,680 Z" fill="#ffffff"/>
      <path d="M0,620 C360,648 770,585 1120,452 L1120,680 L0,680 Z" fill="var(--band)"/>
    </svg>

    <div class="brand">
      <span class="brand__name">STUDIO 847</span>
      <span class="brand__dot"></span>
    </div>

    <div class="person">
      <h1 class="person__name">Martin Kovalenko</h1>
      <p class="person__role">Marketer, Business Strategist</p>
      <address class="person__address">Derveni, 14, 2385,<br>Strovolia Nicosia Cyprus</address>
    </div>

    <div class="divider"></div>

    <ul class="contact">
      <li class="contact__item">
        <svg class="contact__icon" viewBox="0 0 24 24" aria-hidden="true"><path d="M6.6 10.8a15.1 15.1 0 0 0 6.6 6.6l2.2-2.2a1 1 0 0 1 1-.25 11.4 11.4 0 0 0 3.6.57 1 1 0 0 1 1 1V20a1 1 0 0 1-1 1A17 17 0 0 1 3 4a1 1 0 0 1 1-1h3.5a1 1 0 0 1 1 1c0 1.25.2 2.45.57 3.57a1 1 0 0 1-.25 1z"/></svg>
        <span>22 418305</span>
      </li>
      <li class="contact__item">
        <svg class="contact__icon" viewBox="0 0 24 24" aria-hidden="true"><path d="M7 1h10a2 2 0 0 1 2 2v18a2 2 0 0 1-2 2H7a2 2 0 0 1-2-2V3a2 2 0 0 1 2-2zm0 4v13h10V5z"/></svg>
        <span>00357 99102354</span>
      </li>
      <li class="contact__item">
        <span class="contact__at">@</span>
        <span>Martin@studio-847.com</span>
      </li>
    </ul>

    <div class="website">Www.studio-847.com</div>
  </section>
</div>
</body>
</html>
```